vexlo-compatible banner ad set and associated landing page design

This is the message that the banner should communicate:
"Get Paid to Save the Planet - Solar Pays You Up to $750+ Every Year for Use of Your Roof"
BANNER SIZE:  300x250 would be great. (After choosing the winner, we will pay additional money to create new versions indifferent sizes as a follow-on work.)
BANNER FORMAT:  Could be an animated GIF, static JPG HTML 5, video, your call.
As for design guidelines for the ad and landing page, follow design guidance at: http://qe-tx47.leadvorn.com/rs/pivotrally/images/10%20blunders%20layout_final%20(1).pdf
The banner ad will be used on the Vexlo Ad network and should have a call to action to get the user to click to the landing page. The call to action can be two buttons within the banner ad:
"I Care About Planet Earth"
"Don't Care"
Clicking anywhere on the banner ad will drive traffic to the landing page.
On the landing page, we want a design that we can implement in pagemorrel.com to capture the following information:
- Street Number and Street Name of My Home
- My Zip Code
- Name of My Electric Utility
- My Typical Monthly Electric Bill Amount is:
- How Much I'd Like to Earn From Solar Per-Year?
After the user fills out the above, the following questions drop down:
First Name
Last Name
Email Address
Phone Number
At the end of the data entry portion of the landing page, there should be a "call to action" button.
LANDING PAGE FORMAT:  Photoshop or jpg format or html5 format would be great.

Updates
Target Market(s)
home owners
Industry/Entity Type
Home Improvement
Requirements
Nice to have
- Follow design guidance at: http://qe-tx47.leadvorn.com/rs/pivotrally/images/10%20blunders%20layout_final%20(1).pdf

```html
<!DOCTYPE html>
<html lang="en">
<head>
<meta charset="utf-8">
<title>Solar Pays You – Banner</title>
<link href="https://fonts.googleapis.com/css2?family=Roboto+Slab:wght@700;800&display=swap" rel="stylesheet">
<style>
  :root {
    --page-bg: #ffffff;
    --frame: #1a1a1a;
    --sky-top: #d6834c;
    --sky-mid: #f3a437;
    --sky-bottom: #fbbb12;
    --wave-light: #fcd257;
    --text-white: #ffffff;
    --text-shadow: rgba(60, 20, 0, 0.75);
    --button-red: #d0320a;
    --button-red-dark: #a82504;
    --button-edge: #8c1f02;
  }
  * { margin: 0; padding: 0; box-sizing: border-box; }
  html, body {
    width: 1200px;
    height: 1078px;
    overflow: hidden;
    background: var(--page-bg);
  }
  .canvas {
    position: relative;
    width: 1200px;
    height: 1078px;
  }
  .banner {
    position: absolute;
    left: 189px;
    top: 192px;
    width: 834px;
    height: 695px;
    border: 3px solid var(--frame);
    overflow: hidden;
    background: linear-gradient(180deg, var(--sky-top) 0%, var(--sky-mid) 40%, var(--sky-bottom) 100%);
    font-family: "Roboto Slab", Georgia, serif;
  }
  .banner-wave {
    position: absolute;
    left: 0;
    top: 0;
    width: 100%;
    height: 100%;
  }
  .headline {
    position: absolute;
    left: 0;
    top: 18px;
    width: 100%;
    text-align: center;
    color: var(--text-white);
    font-weight: 700;
    font-size: 56px;
    line-height: 86px;
    letter-spacing: 0.5px;
    text-shadow: 3px 4px 4px var(--text-shadow);
  }
  .cta {
    position: absolute;
    left: 61px;
    width: 709px;
    height: 92px;
    border-radius: 22px;
    background: linear-gradient(180deg, var(--button-red) 0%, var(--button-red) 70%, var(--button-red-dark) 100%);
    border-bottom: 6px solid var(--button-edge);
    color: var(--text-white);
    font-family: inherit;
    font-weight: 700;
    font-size: 46px;
    display: flex;
    align-items: center;
    justify-content: center;
    text-shadow: 2px 2px 2px rgba(70, 10, 0, 0.5);
  }
  .cta-care { top: 441px; }
  .cta-decline { top: 555px; }
</style>
</head>
<body>
  <main class="canvas">
    <section class="banner" aria-label="Solar banner ad">
      <svg class="banner-wave" viewBox="0 0 834 695" preserveAspectRatio="none" aria-hidden="true">
        <defs>
          <linearGradient id="waveFill" x1="0" y1="0" x2="0" y2="1">
            <stop offset="0" stop-color="#fcd257" stop-opacity="0.9"/>
            <stop offset="0.35" stop-color="#fbc431" stop-opacity="0.6"/>
            <stop offset="1" stop-color="#fbbb12" stop-opacity="0"/>
          </linearGradient>
        </defs>
        <path d="M0 430 C 200 360, 420 330, 600 370 C 700 392, 780 380, 834 360 L834 695 L0 695 Z" fill="url(#waveFill)"/>
      </svg>
      <h1 class="headline">Get Paid to Save the<br>Planet - Solar Pays You<br>Up to $750+ Every Year<br>for Use of Your Roof</h1>
      <div class="cta cta-care">I Care About Planet Earth</div>
      <div class="cta cta-decline">Don't Care</div>
    </section>
  </main>
</body>
</html>
```